Talvon Crest Real estate in need of Logo design

I just started a new real estate brokerage company and need a professional, new logo design that I can incorporate through all forms of marketing and branding. I would like the business card to use both Matte finish and high gloss.

```html
<!DOCTYPE html>
<html lang="en">
<head>
<meta charset="utf-8">
<title>Talvon Crest Real Estate – Business Card</title>
<link rel="stylesheet" href="https://fonts.googleapis.com/css2?family=Cinzel:wght@500&family=Lato:wght@400&display=swap">
<style>
  :root {
    --backdrop: #2e2e2e;
    --card-white: #ffffff;
    --brand-blue: #12317a;
    --brand-grey: #939598;
    --text-dark: #222222;
    --rule-grey: #9a9a9a;
    --rule-blue: #8a8fb8;
  }
  * { margin: 0; padding: 0; box-sizing: border-box; }
  html, body { width: 1200px; height: 1200px; overflow: hidden; }
  body { background: var(--backdrop); position: relative; font-family: "Lato", Arial, sans-serif; }

  .card { position: absolute; top: 310px; width: 365px; height: 594px; }
  .card-front { left: 234px; background: var(--card-white); text-align: center; }
  .card-back { left: 628px; background: var(--brand-blue); overflow: hidden; }

  .brand-mark { position: absolute; left: 155px; top: 420px; width: 56px; height: 56px; background: var(--brand-blue); }
  .front-inner { position: absolute; left: 0; right: 0; top: 0; }
  .brand-name {
    position: absolute; left: 0; right: 0; top: 522px;
    font-family: "Cinzel", Georgia, serif; font-weight: 500; color: var(--brand-blue);
    font-size: 29px; line-height: 32px; letter-spacing: 0.5px;
  }
  .brand-name .line-two { display: block; font-size: 20px; letter-spacing: 2px; line-height: 26px; }

  .person-name {
    position: absolute; left: 0; right: 0; top: 332px;
    font-family: "Cinzel", Georgia, serif; font-weight: 500; color: var(--brand-blue);
    font-size: 25px; letter-spacing: 0.3px;
  }
  .person-role { position: absolute; left: 0; right: 0; top: 360px; font-size: 16px; color: var(--text-dark); }

  .contact-icons { position: absolute; left: 86px; top: 395px; width: 192px; height: 26px; }

  .contact-lines { position: absolute; left: 0; right: 0; top: 432px; font-size: 16.5px; line-height: 22px; color: var(--text-dark); }
  .contact-rule { position: absolute; left: 88px; width: 195px; top: 507px; border-top: 1px solid var(--rule-blue); }
  .address { position: absolute; left: 0; right: 0; top: 518px; font-size: 16.5px; line-height: 22px; color: var(--text-dark); }

  .back-band { position: absolute; left: 0; top: 0; width: 100%; height: 270px; background: var(--brand-grey); }
  .back-name {
    position: absolute; left: 0; right: 0; top: 300px; text-align: center;
    font-family: "Cinzel", Georgia, serif; font-weight: 500; color: var(--card-white);
    font-size: 34px; line-height: 40px; letter-spacing: 1px;
  }
</style>
</head>
<body>
  <section class="card card-front">
    <div class="brand-mark" style="left:155px; top:110px;"></div>
    <h1 class="brand-name" style="top:205px;">Talvon Crest<span class="line-two">Real Estate</span></h1>

    <h2 class="person-name">Marcus Ellery</h2>
    <p class="person-role">Managing Director</p>

    <svg class="contact-icons" viewBox="0 0 192 26" aria-hidden="true">
      <line x1="0" y1="13" x2="52" y2="13" stroke="var(--rule-grey)" stroke-width="1"/>
      <line x1="140" y1="13" x2="192" y2="13" stroke="var(--rule-grey)" stroke-width="1"/>
      <circle cx="69" cy="13" r="12" fill="var(--brand-blue)"/>
      <path d="M62 10 q7 -6 14 0 l-2 3 h-2 l-1 -2 h-4 l-1 2 h-2z M64 14 h10 v4 h-10z" fill="#fff"/>
      <circle cx="96" cy="13" r="12" fill="var(--brand-blue)"/>
      <rect x="89" y="8" width="14" height="10" fill="none" stroke="#fff" stroke-width="1.5"/>
      <path d="M89 8 l7 6 l7 -6" fill="none" stroke="#fff" stroke-width="1.5"/>
      <circle cx="123" cy="13" r="12" fill="var(--brand-blue)"/>
      <circle cx="123" cy="13" r="6.5" fill="none" stroke="#fff" stroke-width="1.5"/>
      <path d="M116.5 13 h13 M123 6.5 q-4 6.5 0 13 M123 6.5 q4 6.5 0 13" fill="none" stroke="#fff" stroke-width="1"/>
    </svg>

    <p class="contact-lines">044-987 210 356<br>info@talvoncrest.com<br>www.talvoncrest.com</p>
    <div class="contact-rule"></div>
    <p class="address">421, Address line here,<br>45452,Country Name</p>
  </section>

  <section class="card card-back">
    <div class="back-band"></div>
    <p class="back-name">Talvon Crest<br>Real Estate</p>
  </section>
</body>
</html>
```